PPC Landing Page For Technology Consultant

Looking for a high converting landing page for PPC and other Web Marketing traffic. Main objective is to complete a contact form on the main page (preferably at the top built into header image but open to ideas).

WORDPRESS ONLY. All Elements from Website (www.velntrabid.example) are available in adobe format)

Target Market(s)

IT Professionals in mid market and enterprise industries

Industry/Entity Type

It Service

Font styles to use
Sans Serif

Requirements
Must have
• Wordpress theme, customizable and re-usable. Will need help implementing the new site in our wordpress subdomain.
• Contact Form prominent and highlighted, as well as other call to actions (call, get a quote etc.)
Nice to have
• Scrolling logo list of our partners, or some other way to highlight to the our deep portfolio of providers (http://www.velntrabid.example/our-suppliers/), Products, Services etc.
• Some Testimonial section would be nice as well.

```html
<!DOCTYPE html>
<html lang="en">
<head>
<meta charset="utf-8">
<title>Velntrabid – Technology Consulting</title>
<link href="https://fonts.googleapis.com/css2?family=Poppins:wght@300;400;500;600;700&family=Open+Sans:wght@400;600&display=swap" rel="stylesheet">
<style>
:root{
  --blue:#0d4fa0;
  --blue-dark:#0a3f82;
  --orange:#f68b1f;
  --ink:#222;
  --muted:#8a8a8a;
  --light:#f4f5f7;
  --white:#fff;
  --red:#ee5a5a;
  --coral:#f47f4f;
  --amber:#f6b13c;
  --yellow:#fbd65a;
  --purple:#9a5cb3;
  --indigo:#5a73c9;
  --sky:#4aa8d9;
  --green:#7dc46a;
}
*{margin:0;padding:0;box-sizing:border-box}
html,body{width:1200px;height:4494px;overflow:hidden}
body{position:relative;font-family:"Poppins",sans-serif;color:var(--ink);background:var(--white)}
.abs{position:absolute}
.topbar{left:0;top:0;width:1200px;height:48px;background:var(--blue);color:var(--white);font-size:13px;display:flex;align-items:center;justify-content:flex-end;gap:34px;padding-right:112px}
.topbar b{font-weight:600}
.nav{left:0;top:48px;width:1200px;height:86px;display:flex;align-items:center;padding:0 112px;border-bottom:1px solid #eee}
.brand{font-weight:700;font-size:34px;color:var(--orange);letter-spacing:-0.5px}
.menu{margin-left:auto;display:flex;gap:17px;font-size:13px;text-transform:uppercase;color:#333}
.menu .on{color:var(--orange)}
.menu-search{margin-left:20px;padding-left:18px;border-left:1px solid #ddd;height:28px;display:flex;align-items:center}
.hero{left:0;top:134px;width:1200px;height:606px;background:linear-gradient(120deg,#c9b39b,#8c7764 45%,#5f534a 70%,#b7a792)}
.hero-box{left:300px;top:296px;width:642px;height:259px;background:rgba(80,80,80,.55);text-align:center;color:var(--white)}
.hero-box h1{font-size:62px;font-weight:600;letter-spacing:2px;margin-top:20px}
.hero-box p{font-family:"Open Sans",sans-serif;font-size:15px;line-height:31px;margin-top:2px}
.btn{display:inline-flex;align-items:center;justify-content:center;border-radius:30px;font-weight:500;color:var(--white)}
.btn-orange{background:var(--orange)}
.btn-blue{background:var(--blue)}
.hero-box .btn{width:170px;height:50px;font-size:15px;margin-top:14px}
.dots-v{left:1127px;top:348px;display:flex;flex-direction:column;gap:15px}
.dots-v i{width:13px;height:13px;border-radius:50%;background:var(--white);display:block}
.dots-v i.on{background:var(--orange)}
.cta{left:112px;top:686px;width:976px;height:174px;background:var(--orange)}
.cta-photo{left:0;top:0;width:300px;height:174px;background:linear-gradient(120deg,#3a6db3,#1d4f95)}
.cta-text{left:447px;top:22px;color:var(--white);font-size:22px;line-height:34px}
.cta-phone{left:447px;top:100px;color:var(--white);font-size:32px;font-weight:600;display:flex;align-items:center;gap:10px}
.cta .btn{left:773px;top:96px;width:154px;height:52px;font-size:14px;font-weight:600;position:absolute}
.intro{left:91px;top:942px;width:275px}
.intro h3{font-size:18px;font-weight:600;letter-spacing:.3px}
.intro .rule{width:60px;height:2px;background:var(--orange);margin:18px 0 20px}
.intro p{font-family:"Open Sans",sans-serif;font-size:11px;color:var(--muted);line-height:26.5px;text-align:justify}
.intro .btn{width:130px;height:52px;font-size:14px;margin-top:20px}
.card{top:944px;width:230px;height:300px;background:var(--white);box-shadow:0 2px 10px rgba(0,0,0,.12)}
.card svg.icon{position:absolute;left:20px;top:18px}
.card h4{position:absolute;left:20px;top:112px;font-size:15px;font-weight:500;color:var(--blue)}
.card p{position:absolute;left:20px;top:142px;width:190px;font-family:"Open Sans",sans-serif;font-size:12px;color:var(--muted);line-height:26.5px;text-align:justify}
.card .go{position:absolute;right:0;bottom:0;width:42px;height:38px;background:var(--orange);display:flex;align-items:center;justify-content:center}
.h2{width:1200px;left:0;text-align:center;font-size:40px;font-weight:600;letter-spacing:1px}
.partner{width:233px;height:82px;background:var(--white);box-shadow:0 1px 6px rgba(0,0,0,.14);display:flex;align-items:center;justify-content:center}
.partner i{width:120px;height:30px;border-radius:4px;background:#d9dde3;display:block}
.dots-h{left:546px;top:1648px;display:flex;gap:11px}
.dots-h i{width:14px;height:14px;border-radius:50%;border:1.5px solid #555;display:block}
.dots-h i.on{background:var(--blue);border-color:var(--blue)}
.banner{left:0;top:1768px;width:1200px;height:513px;border-radius:22px;background:linear-gradient(90deg,#6c7785,#8a929c 45%,#2d3c55 75%,#4b5a70)}
.banner h2{position:absolute;left:112px;top:126px;color:var(--white);font-size:41px;font-weight:500;line-height:52px}
.banner p{position:absolute;left:112px;top:244px;width:520px;color:var(--white);font-family:"Open Sans",sans-serif;font-size:15px;line-height:35px}
.banner .btn{position:absolute;left:112px;top:325px;width:153px;height:49px;font-size:15px}
.portfolio{left:0;top:2281px;width:1200px;height:853px;background:var(--light)}
.hub{left:435px;top:2596px;width:330px;height:330px;border-radius:50%;background:var(--white);box-shadow:0 0 20px rgba(0,0,0,.06);display:flex;align-items:center;justify-content:center}
.hub span{font-size:50px;font-weight:700;color:var(--orange)}
.pill{height:94px;width:265px;border-radius:47px;color:var(--white);font-size:12px;font-weight:500;display:flex;align-items:center;text-transform:uppercase;line-height:20px}
.pill.l{padding-left:32px}
.pill.r{padding-left:110px}
.pill .ic{position:absolute;top:7px;width:80px;height:80px;border-radius:50%;background:var(--white);display:flex;align-items:center;justify-content:center}
.pill.l .ic{right:7px}
.pill.r .ic{left:7px}
.testi{left:0;top:3134px;width:1200px;height:496px;background:var(--blue);color:var(--white);text-align:center}
.testi h2{margin-top:92px;font-size:40px;font-weight:600}
.testi .quote{width:890px;margin:26px auto 0;font-family:"Open Sans",sans-serif;font-size:14.5px;line-height:34.5px}
.testi .who{margin-top:14px;font-size:13px;font-weight:600}
.testi .role{font-size:13px;margin-top:6px;font-family:"Open Sans",sans-serif}
.arrow{top:3370px}
.contact{left:0;top:3630px;width:1200px;height:612px;background:linear-gradient(90deg,#3a3e45,#4b4f55 50%,#3c4046)}
.contact h2{position:absolute;left:0;width:1200px;text-align:center;top:80px;color:var(--white);font-size:40px;font-weight:600}
.field{border:1px solid #9a9da2;color:#d7d7d7;font-size:14px;padding-left:15px;display:flex;align-items:center;width:364px;height:51px}
.field.msg{align-items:flex-start;padding-top:16px;width:746px;height:152px}
.forgot{left:241px;top:4102px;color:var(--white);font-size:14px}
.send{left:609px;top:4090px;width:364px;height:49px;background:var(--blue);color:var(--white);font-weight:600;font-size:15px;display:flex;align-items:center;justify-content:center}
.foot-brand{left:112px;top:4322px}
.foot-brand .brand{font-size:42px;line-height:50px}
.foot-tagline{left:122px;top:4376px;font-size:15px;letter-spacing:1.5px;color:var(--ink)}
.foot-menu{left:457px;top:4344px;display:flex;gap:17px;font-size:13px;text-transform:uppercase}
.copy{left:0;width:1200px;top:4412px;text-align:center;font-size:14px;color:#666}
.ver{left:1110px;top:4416px;font-size:11px;color:#999}
</style>
</head>
<body>

<header class="abs topbar">
  <span>&#9742; CALL FOR IMMEDIATE SERVICE: <b>1-800-555-0142</b></span>
  <span>&#128100; LOG IN</span>
</header>

<nav class="abs nav">
  <div class="brand">Velntrabid</div>
  <div class="menu">
    <span class="on">Home</span><span>Technology</span><span>Solutions</span><span>Suppliers</span><span>Testimonials</span><span>Partnership</span><span>Contact Us</span>
  </div>
  <div class="menu-search">
    <svg width="16" height="16" viewBox="0 0 16 16" fill="none" stroke="#888" stroke-width="1.6"><circle cx="7" cy="7" r="5"/><path d="M11 11l4 4"/></svg>
  </div>
</nav>

<section class="abs hero" role="img" aria-label="Photo of a consulting team smiling around an office desk"></section>
<div class="abs hero-box">
  <h1>VELNTRABID</h1>
  <p>Leverage better-than-direct pricing and post-sales support<br>from nearly every ISP, VoIP and Cloud Provider.</p>
  <span class="btn btn-orange">Get Started &#9432;</span>
</div>
<div class="abs dots-v"><i></i><i class="on"></i><i></i><i></i><i></i></div>

<section class="abs cta">
  <div class="abs cta-photo" role="img" aria-label="Photo of a support agent wearing a headset"></div>
  <svg class="abs" style="left:230px;top:0" width="170" height="174" viewBox="0 0 170 174"><polygon points="0,0 70,0 157,87 70,174 0,174 0,0" fill="var(--blue)"/><polygon points="70,0 80,0 167,87 80,174 70,174 157,87" fill="#fff"/></svg>
  <div class="abs cta-text">We do the legwork. You save up to 70% on<br>connectivity, voice and cloud</div>
  <div class="abs cta-phone"><svg width="26" height="26" viewBox="0 0 24 24" fill="none" stroke="#fff" stroke-width="1.8"><path d="M5 3h4l2 5-2.5 1.5a11 11 0 0 0 6 6L16 13l5 2v4a2 2 0 0 1-2 2A16 16 0 0 1 3 5a2 2 0 0 1 2-2z"/></svg>1-800-555-0142</div>
  <span class="btn btn-blue">GET QUOTES &rsaquo;</span>
</section>

<section class="abs intro">
  <h3>FREE CONSULTING &amp; DESIGN</h3>
  <div class="rule"></div>
  <p>Nemo enim ipsam voluptatem quia voluptas sit aspernatur aut odit aut fugit, sed quia consequuntur magni dolores eos qui ratione voluptatem sequi nesciunt. Neque porro quisquam est, qui dolorem ipsum quia dolor sit amet, consectetur, est, qui dolorem ipsum quia dolor sit amet, consectetur,</p>
  <span class="btn btn-orange">Learn More</span>
</section>

<article class="abs card" style="left:387px">
  <svg class="icon" width="84" height="84" viewBox="0 0 84 84" fill="none" stroke="var(--blue)" stroke-width="2"><circle cx="28" cy="40" r="11"/><path d="M8 80v-10a18 18 0 0 1 40 0v10z"/><rect x="44" y="6" width="32" height="22" rx="2"/><path d="M50 14h20M50 20h14M50 28l-4 6"/></svg>
  <h4>TRUSTED ADVISOR</h4>
  <p>Take advantage longstanding relationships with hundreds of ISP, VoIP, and Cloud providers for better-than-direct</p>
  <span class="go"><svg width="18" height="12" viewBox="0 0 18 12" fill="none" stroke="#fff" stroke-width="1.8"><path d="M1 6h15M11 1l5 5-5 5"/></svg></span>
</article>
<article class="abs card" style="left:637px">
  <svg class="icon" width="84" height="84" viewBox="0 0 84 84" fill="none" stroke="var(--blue)" stroke-width="2"><circle cx="32" cy="32" r="24"/><path d="M8 32h48M32 8c-10 12-10 36 0 48M32 8c10 12 10 36 0 48"/><circle cx="52" cy="52" r="12"/><path d="M61 61l14 14"/></svg>
  <h4>GLOBAL REACH</h4>
  <p>Deep product reach from hundreds service providers gives you a competitive edge on a global scale.</p>
  <span class="go"><svg width="18" height="12" viewBox="0 0 18 12" fill="none" stroke="#fff" stroke-width="1.8"><path d="M1 6h15M11 1l5 5-5 5"/></svg></span>
</article>
<article class="abs card" style="left:884px">
  <svg class="icon" width="84" height="84" viewBox="0 0 84 84" fill="none" stroke="var(--blue)" stroke-width="2"><circle cx="40" cy="34" r="22"/><circle cx="40" cy="34" r="9"/><path d="M40 6v6M40 56v6M12 34h6M62 34h6M20 14l4 4M60 14l-4 4M32 62h16v10H32z"/></svg>
  <h4>RIGHT-FIT TECHNOLOGY</h4>
  <p>We've seen it all. Our expertise and geographies, suppliers, industries, and verticals which means solve your problems.</p>
  <span class="go"><svg width="18" height="12" viewBox="0 0 18 12" fill="none" stroke="#fff" stroke-width="1.8"><path d="M1 6h15M11 1l5 5-5 5"/></svg></span>
</article>

<h2 class="abs h2" style="top:1334px">OUR PARTNERS</h2>
<div class="abs partner" style="left:112px;top:1416px"><i></i></div>
<div class="abs partner" style="left:358px;top:1416px"><i></i></div>
<div class="abs partner" style="left:603px;top:1416px"><i></i></div>
<div class="abs partner" style="left:849px;top:1416px"><i></i></div>
<div class="abs partner" style="left:112px;top:1514px"><i></i></div>
<div class="abs partner" style="left:358px;top:1514px"><i></i></div>
<div class="abs partner" style="left:603px;top:1514px;border-bottom:3px solid var(--blue)"><i></i></div>
<div class="abs partner" style="left:849px;top:1514px"><i></i></div>
<div class="abs dots-h"><i></i><i></i><i class="on"></i><i></i><i></i></div>

<section class="abs banner">
  <div class="abs" style="left:0;top:0;width:1200px;height:513px;border-radius:22px" role="img" aria-label="Photo of a smiling businessman in a suit at an office"></div>
  <h2>LEADING PATH IS<br>VELNTRABID COMPANY</h2>
  <p>All of this is at no cost to you, better-than-direct pricing, and, most importantly, with a deep commitment to advocacy for our clients</p>
  <span class="btn btn-blue">Get Quotes &rsaquo;</span>
</section>

<section class="abs portfolio"></section>
<h2 class="abs h2" style="top:2370px">DEEP PRODUCT PORTFOLIO</h2>
<svg class="abs" style="left:0;top:2281px" width="1200" height="853" viewBox="0 0 1200 853" fill="none" stroke="#444" stroke-width="2">
  <path d="M258 232 A52 52 0 0 0 258 330"/><path d="M523 218 A52 52 0 0 1 523 330"/>
  <path d="M160 433 A50 50 0 0 0 160 530"/><path d="M426 323 A52 52 0 0 1 426 433"/>
  <path d="M426 539 A52 52 0 0 1 426 645"/><path d="M258 547 A52 52 0 0 0 258 650"/>
  <path d="M523 647 A52 52 0 0 1 523 741"/>
  <path d="M942 232 A52 52 0 0 1 942 330"/><path d="M677 218 A52 52 0 0 0 677 330"/>
  <path d="M1040 433 A50 50 0 0 1 1040 530"/><path d="M774 323 A52 52 0 0 0 774 433"/>
  <path d="M774 539 A52 52 0 0 0 774 645"/><path d="M942 547 A52 52 0 0 1 942 650"/>
  <path d="M677 647 A52 52 0 0 0 677 741"/>
</svg>
<div class="abs hub"><span>Velntrabid</span></div>

<div class="abs pill l" style="left:258px;top:2499px;background:var(--blue)">Telecommunications<br>Consulting<span class="ic"><svg width="40" height="40" viewBox="0 0 40 40" fill="none" stroke="var(--blue)" stroke-width="2"><circle cx="20" cy="12" r="6"/><path d="M8 36v-6a12 12 0 0 1 24 0v6"/></svg></span></div>
<div class="abs pill l" style="left:160px;top:2604px;background:var(--red)">SIP Trunking<span class="ic"><svg width="40" height="40" viewBox="0 0 40 40" fill="none" stroke="var(--red)" stroke-width="2"><path d="M10 30a7 7 0 0 1 0-14 10 10 0 0 1 19-2 8 8 0 0 1 1 16z"/><path d="M20 30V18M16 22l4-4 4 4"/></svg></span></div>
<div class="abs pill l" style="left:112px;top:2714px;background:var(--coral);padding-left:90px">MPLS<span class="ic"><svg width="44" height="44" viewBox="0 0 44 44" fill="none" stroke="var(--coral)" stroke-width="2"><circle cx="22" cy="22" r="17"/><path d="M5 22h34M22 5c-8 9-8 25 0 34M22 5c8 9 8 25 0 34"/></svg></span></div>
<div class="abs pill l" style="left:160px;top:2820px;background:var(--amber)">Dedicated Internet<br>Access<span class="ic"><svg width="40" height="40" viewBox="0 0 40 40" fill="none" stroke="var(--amber)" stroke-width="3"><circle cx="12" cy="28" r="3" fill="var(--amber)"/><path d="M10 18a12 12 0 0 1 12 12M10 9a21 21 0 0 1 21 21"/></svg></span></div>
<div class="abs pill l" style="left:258px;top:2928px;background:var(--yellow)">Private Networks<span class="ic"><svg width="40" height="40" viewBox="0 0 40 40" fill="none" stroke="var(--yellow)" stroke-width="2"><path d="M10 30a7 7 0 0 1 0-14 10 10 0 0 1 19-2 8 8 0 0 1 1 16z"/><path d="M20 18v8M16 22h8"/></svg></span></div>

<div class="abs pill r" style="left:675px;top:2499px;background:var(--purple)">Advanced 24/7<br>Monitoring<span class="ic"><svg width="40" height="40" viewBox="0 0 40 40" fill="none" stroke="var(--purple)" stroke-width="2"><circle cx="20" cy="20" r="14"/><text x="20" y="24" font-size="10" text-anchor="middle" fill="var(--purple)" stroke="none" font-family="Poppins,sans-serif">24/7</text></svg></span></div>
<div class="abs pill r" style="left:773px;top:2604px;background:var(--indigo);padding-left:135px">Failover<span class="ic"><svg width="40" height="40" viewBox="0 0 40 40" fill="none" stroke="var(--indigo)" stroke-width="2"><rect x="6" y="8" width="28" height="24" rx="2"/><path d="M6 15h28M14 8v7"/></svg></span></div>
<div class="abs pill r" style="left:820px;top:2714px;background:var(--sky)">Unified Communi<br>cations<span class="ic"><svg width="40" height="40" viewBox="0 0 40 40" fill="none" stroke="var(--sky)" stroke-width="2"><rect x="12" y="5" width="16" height="30" rx="2"/><circle cx="20" cy="20" r="4"/></svg></span></div>
<div class="abs pill r" style="left:773px;top:2820px;background:var(--green)">Hosted Voice<span class="ic"><svg width="40" height="40" viewBox="0 0 24 24" fill="none" stroke="var(--green)" stroke-width="1.6"><path d="M5 3h4l2 5-2.5 1.5a11 11 0 0 0 6 6L16 13l5 2v4a2 2 0 0 1-2 2A16 16 0 0 1 3 5a2 2 0 0 1 2-2z"/></svg></span></div>
<div class="abs pill r" style="left:675px;top:2928px;background:var(--orange)">Global Private<br>Connectivity<span class="ic"><svg width="40" height="40" viewBox="0 0 40 40" fill="none" stroke="var(--orange)" stroke-width="2"><circle cx="10" cy="28" r="4"/><circle cx="30" cy="12" r="4"/><circle cx="30" cy="30" r="4"/><path d="M13 26l14-12M14 28h12"/></svg></span></div>

<section class="abs testi">
  <h2>CLIENT TESTIMONIALS</h2>
  <p class="quote">&ldquo;I've recently been working with Velntrabid to assist with providing communications services to client offices in the US. Their level of customer service has been excellent, with rapid responses to questions &amp; requests. They have done a great job of providing numerous options, and have been very patient and helpful when I 've had questions about services, terminology, etc. Having a broker that knows the market, the providers, and the products has been a godsend, and having all the options priced out along with recommendations makes the whole process smooth&rdquo;</p>
  <p class="who">– DANA WHITFIELD</p>
  <p class="role">IT Manager – International MSP</p>
</section>
<svg class="abs arrow" style="left:68px" width="16" height="26" viewBox="0 0 16 26" fill="none" stroke="#fff" stroke-width="2"><path d="M13 2L3 13l10 11"/></svg>
<svg class="abs arrow" style="left:1106px" width="16" height="26" viewBox="0 0 16 26" fill="none" stroke="#fff" stroke-width="2"><path d="M3 2l10 11L3 24"/></svg>

<section class="abs contact" role="img" aria-label="Dimmed photo of professionals in a meeting">
  <h2>GET IN TOUCH</h2>
</section>
<div class="abs field" style="left:227px;top:3781px">First Name</div>
<div class="abs field" style="left:609px;top:3781px">Last Name</div>
<div class="abs field" style="left:227px;top:3849px">Email</div>
<div class="abs field" style="left:609px;top:3849px">Phone</div>
<div class="abs field msg" style="left:227px;top:3915px">Message</div>
<div class="abs forgot">Forgot your password?</div>
<div class="abs send">SEND</div>

<footer>
  <div class="abs foot-brand"><div class="brand">Velntrabid</div></div>
  <div class="abs foot-tagline">CONNECT &amp; CONSULT</div>
  <div class="abs foot-menu"><span>Home</span><span>Technology Solutions</span><span>Suppliers</span><span>Testimonials</span><span>Partnership</span><span>Contact Us</span></div>
  <div class="abs copy">&copy; 2020 All Rights Reserved</div>
  <div class="abs ver">c40</div>
</footer>

</body>
</html>
```